Orva Business Card

we need a business card for flooring business called Orva Flooring, the design should be black and white. we have 2 locations

Larkfield Showroom
527 Kellerman Road,
Larkfield VIC 3186

Tessmore Showroom
462 Bramwell Hwy,
Tessmore VIC 3219

email : sales@orvaflooring.com.au
(03) 9471 2830

Please inform we sell , Laminate, Hybrid, Timber, carpet and commercial flooring

```html
<!DOCTYPE html>
<html lang="en">
<head>
<meta charset="utf-8">
<title>Orva Flooring Business Card</title>
<link href="https://fonts.googleapis.com/css2?family=Poppins:wght@400;600&display=swap" rel="stylesheet">
<style>
  :root {
    --stage: #9a9a9a;
    --ink: #000000;
    --paper: #ffffff;
  }
  * { margin: 0; padding: 0; box-sizing: border-box; }
  html, body {
    width: 1200px;
    height: 1200px;
    overflow: hidden;
    background: var(--stage);
    font-family: "Poppins", sans-serif;
  }
  .card {
    position: absolute;
    left: 220px;
    width: 758px;
    height: 455px;
  }
  .card--front { top: 108px; background: var(--ink); color: var(--paper); }
  .card--back { top: 642px; background: var(--paper); color: var(--ink); }

  .wordmark {
    position: absolute;
    width: 240px;
    text-align: center;
    font-weight: 400;
    line-height: 1;
  }
  .wordmark__name {
    display: block;
    font-size: 80px;
    letter-spacing: 4px;
    padding-left: 4px;
  }
  .wordmark__trade {
    display: block;
    font-size: 42px;
    margin-top: 10px;
  }
  .card--front .wordmark { left: 39px; top: 193px; }
  .card--back .wordmark { left: 258px; top: 111px; }

  .divider-vertical {
    position: absolute;
    left: 333px;
    top: 94px;
    width: 7px;
    height: 267px;
    border-left: 1px solid var(--paper);
    border-right: 3px solid var(--paper);
  }

  .contact-list { list-style: none; }
  .contact {
    position: absolute;
    left: 406px;
    display: flex;
    align-items: flex-start;
    gap: 10px;
    font-size: 19.5px;
    line-height: 34px;
  }
  .contact__icon { width: 30px; height: 30px; margin-top: 2px; flex: none; }
  .contact__title { font-weight: 600; }
  .contact--phone { top: 78px; }
  .contact--email { top: 123px; }
  .contact--north { top: 171px; }
  .contact--south { top: 284px; }

  .divider-horizontal {
    position: absolute;
    left: 243px;
    top: 288px;
    width: 266px;
    height: 7px;
    border-top: 1px solid var(--ink);
    border-bottom: 3px solid var(--ink);
  }
  .range {
    position: absolute;
    left: 0;
    top: 334px;
    width: 100%;
    text-align: center;
    font-size: 22px;
    line-height: 34px;
  }
</style>
</head>
<body>

<section class="card card--front" aria-label="Card front">
  <div class="wordmark">
    <span class="wordmark__name">ORVA</span>
    <span class="wordmark__trade">FLOORING</span>
  </div>

  <div class="divider-vertical"></div>

  <ul class="contact-list">
    <li class="contact contact--phone">
      <svg class="contact__icon" viewBox="0 0 30 30" fill="none" stroke="#fff" stroke-width="1.6">
        <circle cx="15" cy="15" r="13.5"/>
        <path d="M10.5 8.5l2.5 0 1 3.5-1.6 1.3a8 8 0 0 0 4.3 4.3l1.3-1.6 3.5 1v2.5a1.5 1.5 0 0 1-1.6 1.5A12 12 0 0 1 9 10.1a1.5 1.5 0 0 1 1.5-1.6z"/>
      </svg>
      <span>(03) 9471 2830</span>
    </li>
    <li class="contact contact--email">
      <svg class="contact__icon" viewBox="0 0 30 30" fill="none" stroke="#fff" stroke-width="1.6">
        <circle cx="15" cy="15" r="13.5"/>
        <rect x="8.5" y="10" width="13" height="10" rx="1"/>
        <path d="M8.5 10l6.5 5.5 6.5-5.5M8.5 20l5-4.5M21.5 20l-5-4.5"/>
      </svg>
      <span>sales@orvaflooring.com.au</span>
    </li>
    <li class="contact contact--north">
      <svg class="contact__icon" viewBox="0 0 30 30" fill="none" stroke="#fff" stroke-width="1.6">
        <circle cx="15" cy="15" r="13.5"/>
        <path d="M15 20s-4.5-4.5-4.5-7.5a4.5 4.5 0 0 1 9 0c0 3-4.5 7.5-4.5 7.5z"/>
        <circle cx="15" cy="12.5" r="1.6"/>
        <path d="M10 22h10"/>
      </svg>
      <span>
        <span class="contact__title">Larkfield Showroom</span><br>
        527 Kellerman Road,<br>
        Larkfield VIC 3186
      </span>
    </li>
    <li class="contact contact--south">
      <svg class="contact__icon" viewBox="0 0 30 30" fill="none" stroke="#fff" stroke-width="1.6">
        <circle cx="15" cy="15" r="13.5"/>
        <path d="M15 20s-4.5-4.5-4.5-7.5a4.5 4.5 0 0 1 9 0c0 3-4.5 7.5-4.5 7.5z"/>
        <circle cx="15" cy="12.5" r="1.6"/>
        <path d="M10 22h10"/>
      </svg>
      <span>
        <span class="contact__title">Tessmore Showroom</span><br>
        462 Bramwell Hwy,<br>
        Tessmore VIC 3219
      </span>
    </li>
  </ul>
</section>

<section class="card card--back" aria-label="Card back">
  <div class="wordmark">
    <span class="wordmark__name">ORVA</span>
    <span class="wordmark__trade">FLOORING</span>
  </div>
  <div class="divider-horizontal"></div>
  <p class="range">We sell Laminate, Hybrid, Timber, Carpet<br>and Commercial flooring</p>
</section>

</body>
</html>
```